Web Design Project - QuorvanTel

We have created an initial website at http://www.quorvantel.com

This project requires you to take the current website and redesigning it to improve the overall look and feel.

Feel free to experiment with everything including:

~ colour schemes
~ layout

The only constraints are

- the text content
- the app icons on /games
- the logo structure (feel free to change the colour schemes / logo image)

In terms of process - please feel free to post concepts / mockups for one page - if this is easier for you to do quickly (without revamping the entire site).

As well as the website, please provide designs for a plazanet page cover and profile picture for http://www.plazanet.com/pages/QuorvanTel/738204619352018

Thanks for the submissions - but we've not quite found what we're looking for.

This site is on which appeals to us - please use this for inspiration: http://bramwexa.com/

Thanks

Reason: I am about to make this project "guaranteed" and want to give more time to submit

Please submit your creative ideas - we look forward to receiving them.

Reason: Hi, Deadline extended so that we can see revisions Thanks

Target Market(s)

Marketing Executives / CEOs of Media Companies

Industry/Entity Type

Games

```html
<!DOCTYPE html>
<html lang="en">
<head>
<meta charset="utf-8">
<title>QuorvanTel — In-play second screen games</title>
<link rel="stylesheet" href="https://fonts.googleapis.com/css2?family=Noto+Sans:ital,wght@0,400;0,700;1,400&family=Arimo:ital,wght@0,400;0,700;1,400&display=swap">
<style>
  :root {
    --ink: #000000;
    --page: #ffffff;
    --brand-green: #12c400;
    --brand-red: #d80000;
    --nav-dark: #0c0c0c;
    --nav-light: #2e2e2e;
    --nav-text: #ffffff;
    --nav-muted: #9a9a9a;
    --drop-bg: rgba(0, 52, 62, 0.92);
    --drop-line: rgba(255, 255, 255, 0.12);
    --green: #13d61a;
    --green-dark: #08b10e;
    --blue: #0f72e0;
    --blue-dark: #0a58bb;
    --orange: #e23a0c;
    --orange-dark: #c02b05;
    --heading: #4a5f95;
    --body: #5a5a5a;
    --footer: #333333;
    --footer-text: #ffffff;
    --footer-soft: #d8d8d8;
    --search-line: #d6d6d6;
  }
  * { box-sizing: border-box; margin: 0; padding: 0; }
  html, body { width: 1141px; height: 1200px; overflow: hidden; background: var(--page); }
  body { position: relative; font-family: "Noto Sans", sans-serif; color: var(--body); }

  .top-rule { position: absolute; left: 0; top: 5px; width: 1141px; height: 5px; background: var(--ink); }

  .brand { position: absolute; left: 56px; top: 56px; width: 170px; display: flex; flex-direction: column; align-items: center; gap: 12px; }
  .brand-mark { width: 56px; height: 56px; background: var(--brand-green); }
  .brand-name { font-family: "Noto Sans", sans-serif; font-weight: 700; font-size: 27px; line-height: 32px; color: var(--brand-green); white-space: nowrap; }

  .tagline { position: absolute; left: 234px; top: 107px; font-family: "Arimo", sans-serif; font-style: italic; font-size: 20px; color: #1a1a1a; white-space: nowrap; }

  .follow-top { position: absolute; right: 45px; top: 53px; display: flex; align-items: center; gap: 12px; font-family: "Arimo", sans-serif; font-size: 13px; color: var(--brand-red); }
  .follow-top .dot { width: 22px; height: 22px; border-radius: 50%; background: #29a9e6; }

  .search { position: absolute; left: 861px; top: 171px; width: 235px; height: 25px; border: 1px solid var(--search-line); font-size: 13px; color: #888; padding: 4px 8px; }
  .search svg { position: absolute; right: 6px; top: 4px; }

  .nav { position: absolute; left: 45px; top: 222px; width: 1051px; height: 56px; background: linear-gradient(var(--nav-light), var(--nav-dark) 60%); border: 5px solid #000; border-radius: 3px; }
  .nav ul { list-style: none; position: relative; height: 100%; }
  .nav li { position: absolute; top: 15px; transform: translateX(-50%); font-weight: 700; font-size: 13.5px; color: var(--nav-text); }
  .nav li.active { color: var(--nav-muted); }

  .hero { position: absolute; left: 45px; top: 281px; width: 1051px; height: 401px; background: linear-gradient(#29c8ee 0%, #6fdcf4 25%, #e6c27a 38%, #1d2540 52%, #5cc22a 64%, #3f9d1c 100%); }
  .hero-shadow { position: absolute; left: 60px; top: 682px; width: 1021px; height: 26px; background: radial-gradient(ellipse at top, rgba(0,0,0,0.28), rgba(0,0,0,0) 70%); }

  .dropdown { position: absolute; left: 704px; top: 273px; width: 179px; list-style: none; border-top: 5px solid #c9c9c9; background: var(--drop-bg); }
  .dropdown li { height: 35px; line-height: 34px; padding-left: 17px; font-weight: 700; font-size: 13px; color: #fff; border-bottom: 1px solid var(--drop-line); letter-spacing: 0.3px; }

  .pager { position: absolute; left: 500px; top: 693px; display: flex; gap: 7px; }
  .pager span { width: 22px; height: 22px; border-radius: 50%; background: var(--blue); box-shadow: inset 0 -2px 3px rgba(0,0,0,0.3); }
  .pager span.current { background: var(--green); }

  .feature { position: absolute; top: 728px; width: 313px; }
  .feature.one { left: 45px; } .feature.two { left: 414px; } .feature.three { left: 783px; }
  .feature-bar { height: 43px; border-radius: 2px; padding: 10px 12px; font-weight: 700; font-size: 15.5px; color: #fff; border: 2px solid; }
  .one .feature-bar { background: var(--green); border-color: var(--green-dark); }
  .two .feature-bar { background: var(--blue); border-color: var(--blue-dark); }
  .three .feature-bar { background: var(--orange); border-color: var(--orange-dark); }
  .feature h3 { margin: 22px 0 0 12px; font-size: 16px; font-weight: 700; color: var(--heading); }
  .feature p { margin: 12px 0 0 12px; font-size: 13.6px; line-height: 20px; color: var(--body); width: 272px; }
  .feature .more { display: block; margin: 17px 0 0 12px; width: 112px; height: 26px; line-height: 24px; text-align: center; font-weight: 700; font-size: 12.5px; color: #fff; border-radius: 2px; }
  .one .more { background: var(--green); } .two .more { background: var(--blue); } .three .more { background: var(--orange); }

  .footer { position: absolute; left: 45px; top: 1000px; width: 1051px; height: 177px; background: var(--footer); border-radius: 3px; font-family: "Arimo", sans-serif; }
  .footer-legal { position: absolute; left: 0; width: 837px; top: 69px; text-align: center; }
  .footer-legal strong { display: block; font-size: 14.5px; color: var(--footer-text); }
  .footer-legal small { display: block; margin-top: 8px; font-size: 12.5px; color: var(--footer-soft); }
  .footer-divider { position: absolute; left: 837px; top: 22px; width: 1px; height: 134px; background: #474747; }
  .footer-side { position: absolute; left: 870px; top: 30px; color: var(--footer-text); font-size: 13.5px; }
  .social { display: flex; gap: 8px; margin-top: 8px; }
  .social span { width: 24px; height: 24px; border-radius: 50%; }
  .footer-links { list-style: none; margin-top: 18px; }
  .footer-links li { margin-bottom: 13px; font-size: 13.5px; }
  .footer-links li::before { content: "▸"; font-size: 8px; margin-right: 6px; vertical-align: 2px; }
</style>
</head>
<body>
  <div class="top-rule"></div>

  <header>
    <div class="brand">
      <span class="brand-mark"></span>
      <span class="brand-name">QuorvanTel</span>
    </div>
    <p class="tagline">Delivering in-play second screen games based on live broadcast events</p>
    <div class="follow-top"><span class="dot"></span><span>Follow us on Chirpline</span></div>
    <div class="search">Search
      <svg width="16" height="16" viewBox="0 0 16 16"><circle cx="9.5" cy="6.5" r="4.5" fill="none" stroke="#999" stroke-width="1.5"/><line x1="6.3" y1="9.7" x2="2" y2="14" stroke="#999" stroke-width="2"/></svg>
    </div>
  </header>

  <nav class="nav">
    <ul>
      <li style="left:232px">HOME</li>
      <li style="left:337px">ABOUT</li>
      <li style="left:442px">GAMES</li>
      <li style="left:565px">SOLUTIONS</li>
      <li class="active" style="left:679px">UPDATE</li>
      <li style="left:796px">CONTACT</li>
    </ul>
  </nav>

  <div class="hero" role="img" aria-label="Illustration of a football match in a floodlit stadium: a striker shoots as the goalkeeper dives beside the goal net"></div>
  <div class="hero-shadow"></div>

  <ul class="dropdown">
    <li>Reformidans</li>
    <li>Iuvaret</li>
    <li>Consequuntur</li>
    <li>Ullamcorper</li>
    <li>Essent</li>
    <li>Gloriatur</li>
  </ul>

  <div class="pager"><span class="current"></span><span></span><span></span><span></span><span></span></div>

  <section class="feature one">
    <div class="feature-bar">Partem Similique</div>
    <h3>Liber quodsi</h3>
    <p>Quo agam facilisis ei, liber quodsi debitis ex est. Labore audire eam in. Case facilisi eleifend te pri, mei ei exerci oportere. Per an ignota postea. Ea duo fugit augue</p>
    <span class="more">Read more</span>
  </section>
  <section class="feature two">
    <div class="feature-bar">Partem Similique</div>
    <h3>Liber quodsi</h3>
    <p>Quo agam facilisis ei, liber quodsi debitis ex est. Labore audire eam in. Case facilisi eleifend te pri, mei ei exerci oportere. Per an ignota postea. Ea duo fugit augue</p>
    <span class="more">Read more</span>
  </section>
  <section class="feature three">
    <div class="feature-bar">Partem Similique</div>
    <h3>Liber quodsi</h3>
    <p>Quo agam facilisis ei, liber quodsi debitis ex est. Labore audire eam in. Case facilisi eleifend te pri, mei ei exerci oportere. Per an ignota postea. Ea duo fugit augue</p>
    <span class="more">Read more</span>
  </section>

  <footer class="footer">
    <div class="footer-legal">
      <strong>Use of this Web site constitutes acceptance of QuorvanTel's Terms of Service and Privacy Policy</strong>
      <small>© Copyright 2012. All rights reserved.</small>
    </div>
    <div class="footer-divider"></div>
    <div class="footer-side">
      Follow us:
      <div class="social">
        <span style="background:#f07f16"></span>
        <span style="background:#3fb3e6"></span>
        <span style="background:#2c4a8c"></span>
        <span style="background:#9a9a9a"></span>
      </div>
      <ul class="footer-links">
        <li>Terms and Conditions</li>
        <li>Privacy Policy</li>
      </ul>
    </div>
  </footer>
</body>
</html>
```